Brand Identity Stationary Package

Hello I'm looking for a full branding package for my Property Management Company. I have a logo but looking to have the following
Business Card
Email signature
Facebook cover photo
Letterhead (word.doc)
#10 Envelope
Pocket Folder - link to 9x12 pocket folder design specs https://www.quillpress.ca/marketing-materials/presentation-folders
would like everything to match and be brand identifiable. The company looks after residential properties/apartments and some commercial properties. Attached is a zip of the files.
For Business Card
Name: Morgan Tillsey
Position: Operations Manager
Number: 1 (506) 384-2971
Email: Morgan@harbrook.ca
Website: Harbrook.ca
Industry/Entity Type
Property Management

```html
<!DOCTYPE html>
<html lang="en">
<head>
<meta charset="UTF-8">
<title>Harbrook Property Management – Pocket Folder</title>
<link href="https://fonts.googleapis.com/css2?family=Montserrat:wght@500;700&family=Roboto:wght@400;500&display=swap" rel="stylesheet">
<style>
  :root {
    --backdrop: #d9d8d8;
    --folder-black: #0b0808;
    --ink-white: #ffffff;
    --brand-green: #7cb342;
    --facade-light: #c9d2d4;
    --facade-warm: #a78a82;
    --facade-dark: #3a3f42;
  }
  * { margin: 0; padding: 0; box-sizing: border-box; }
  html, body {
    width: 1200px;
    height: 847px;
    overflow: hidden;
    background: var(--backdrop);
  }
  .folder-spread {
    position: absolute;
    left: 30px;
    top: 43px;
    width: 1140px;
    height: 760px;
    display: flex;
    box-shadow: 0 10px 30px rgba(0,0,0,0.25);
  }
  .folder-panel {
    position: relative;
    width: 570px;
    height: 760px;
    background: var(--folder-black);
    overflow: hidden;
  }
  .folder-panel--back { border-right: 1px solid #1c1818; }

  .contact-block {
    position: absolute;
    left: 0;
    right: 0;
    bottom: 92px;
    text-align: center;
    font-family: "Roboto", sans-serif;
    font-size: 12.5px;
    line-height: 1.45;
    color: var(--ink-white);
  }
  .contact-block__company {
    color: var(--brand-green);
    font-weight: 500;
  }
  .contact-block__row { display: flex; justify-content: center; align-items: center; gap: 5px; }
  .contact-icon { width: 11px; height: 11px; fill: var(--brand-green); }

  .brand-lockup {
    position: absolute;
    top: 100px;
    left: 80px;
    width: 290px;
    text-align: center;
    font-family: "Montserrat", sans-serif;
    color: var(--ink-white);
  }
  .brand-lockup__name {
    font-size: 38px;
    font-weight: 700;
    letter-spacing: 3px;
    line-height: 1;
  }
  .brand-lockup__tagline {
    margin-top: 6px;
    font-size: 9px;
    font-weight: 500;
    letter-spacing: 5.2px;
  }

  .cover-photo {
    position: absolute;
    left: 0;
    bottom: 0;
    width: 570px;
    height: 760px;
  }
</style>
</head>
<body>
  <main class="folder-spread">
    <section class="folder-panel folder-panel--back">
      <address class="contact-block">
        <div class="contact-block__company">Harbrook Ltd</div>
        <div>48 Cedar Cove Lane,&nbsp; Maple Ridge, ON L7K 3P4</div>
        <div class="contact-block__row">
          <svg class="contact-icon" viewBox="0 0 24 24" aria-hidden="true"><path d="M6.6 10.8a15.1 15.1 0 0 0 6.6 6.6l2.2-2.2a1 1 0 0 1 1-.25 11.4 11.4 0 0 0 3.6.57 1 1 0 0 1 1 1V20a1 1 0 0 1-1 1A17 17 0 0 1 3 4a1 1 0 0 1 1-1h3.5a1 1 0 0 1 1 1c0 1.25.2 2.45.57 3.57a1 1 0 0 1-.25 1z"/></svg>
          <span>1 (506) 384-2971</span>
          <svg class="contact-icon" viewBox="0 0 24 24" aria-hidden="true"><path d="M2 5h20v14H2z M2 5l10 8 10-8" fill="var(--brand-green)" stroke="var(--folder-black)" stroke-width="1.5"/></svg>
          <span>Morgan@harbrook.ca</span>
        </div>
        <div>www.harbrook.ca</div>
      </address>
    </section>

    <section class="folder-panel folder-panel--front">
      <div class="brand-lockup">
        <div class="brand-lockup__name">HARBROOK</div>
        <div class="brand-lockup__tagline">PROPERTY MANAGEMENT</div>
      </div>

      <svg class="cover-photo" viewBox="0 0 570 760" role="img" aria-label="Photograph looking up at the angled corner of a modern building with layered glass and pale facade panels">
        <defs>
          <linearGradient id="facadeTone" x1="0" y1="0" x2="1" y2="0.4">
            <stop offset="0" stop-color="var(--facade-light)"/>
            <stop offset="0.5" stop-color="var(--facade-dark)"/>
            <stop offset="1" stop-color="var(--facade-warm)"/>
          </linearGradient>
        </defs>
        <polygon points="250,400 570,660 570,760 110,760" fill="url(#facadeTone)"/>
      </svg>
    </section>
  </main>
</body>
</html>
```